Business Cards and Stationary
Silver Pine
Professional
Tom Feaster, P.G.
Founder
4718 Wexley Lane
Golden, Colorado 80401
tfeaster@silverpinenviroq.com
www.silverpinenviroq.com
Consulting Compliance Training

```html
<!DOCTYPE html>
<html lang="en">
<head>
<meta charset="utf-8">
<title>Silver Pine – Stationery Set</title>
<link href="https://fonts.googleapis.com/css2?family=Open+Sans:wght@400;600;800&display=swap" rel="stylesheet">
<style>
  :root {
    --maroon: #7a1414;
    --maroon-dark: #5e0e0e;
    --blush: #f2d6d2;
    --paper: #ffffff;
    --window: #ececec;
    --ink: #4a4a4a;
    --backdrop: #c8c8c8;
  }
  * { box-sizing: border-box; margin: 0; padding: 0; }
  html, body { width: 1200px; height: 840px; overflow: hidden; }
  body {
    position: relative;
    background: var(--backdrop);
    font-family: "Open Sans", Arial, sans-serif;
    color: var(--ink);
  }
  .piece { position: absolute; background: var(--paper); overflow: hidden; box-shadow: 0 1px 3px rgba(0,0,0,.18); }

  .wordmark {
    font-family: "Open Sans", Arial, sans-serif;
    font-weight: 800;
    color: var(--maroon);
    letter-spacing: .5px;
    white-space: nowrap;
    display: flex;
    align-items: center;
  }
  .wordmark .mark-dot { border-radius: 50%; background: var(--maroon); margin-right: 6px; flex: none; }

  .faint-disc { position: absolute; border-radius: 50%; background: var(--blush); }

  /* Envelope */
  .envelope-flap { position: absolute; left: 96px; top: 60px; width: 492px; height: 60px; }
  .envelope { left: 96px; top: 115px; width: 492px; height: 300px; box-shadow: none; border-bottom: 3px solid var(--maroon-dark); }
  .envelope .faint-disc { left: 30px; top: -40px; width: 230px; height: 230px; }
  .envelope .wordmark { position: absolute; right: 12px; top: 88px; font-size: 21px; }
  .envelope .wordmark .mark-dot { width: 12px; height: 12px; }
  .envelope-window { position: absolute; left: 101px; top: 168px; width: 223px; height: 76px; background: var(--window); border: 1px solid #d8d8d8; border-radius: 3px; }
  .envelope-footer { position: absolute; left: 0; right: 0; bottom: 9px; text-align: center; font-size: 6.5px; color: var(--ink); }

  /* Letterhead */
  .letterhead { left: 624px; top: 67px; width: 497px; height: 706px; border-top: 6px solid var(--maroon); border-bottom: 6px solid var(--maroon); }
  .letterhead .wordmark { position: absolute; left: 34px; top: 62px; font-size: 21px; }
  .letterhead .wordmark .mark-dot { width: 12px; height: 12px; }
  .letterhead-rule { position: absolute; left: 205px; right: 0; top: 78px; height: 1px; background: var(--maroon); }
  .letterhead .faint-disc { left: 0; top: 305px; width: 410px; height: 410px; }
  .letterhead-footer { position: absolute; left: 0; right: 0; bottom: 8px; text-align: center; font-size: 6.5px; color: var(--ink); }

  /* Business cards */
  .card-front { left: 96px; top: 480px; width: 216px; height: 132px; }
  .card-front .wordmark { position: absolute; left: 10px; top: 50px; font-size: 11px; }
  .card-front .wordmark .mark-dot { width: 7px; height: 7px; margin-right: 3px; }
  .card-details { position: absolute; left: 118px; top: 24px; font-size: 6px; line-height: 1.5; }
  .card-name { font-weight: 600; font-size: 7px; color: #222; }
  .card-role { margin-bottom: 8px; }
  .card-address { margin-bottom: 8px; }

  .card-back { left: 331px; top: 480px; width: 216px; height: 132px; background: var(--maroon); }
  .card-back .faint-disc { left: -8px; top: -12px; width: 110px; height: 110px; background: #c98c86; opacity: .75; }
  .card-web { position: absolute; right: 10px; bottom: 14px; font-size: 6px; color: #f3dede; }
</style>
</head>
<body>

  <!-- Envelope -->
  <svg class="envelope-flap" viewBox="0 0 492 60" aria-hidden="true">
    <path d="M0 60 Q0 4 46 2 Q246 -8 446 2 Q492 4 492 60 Z" fill="var(--maroon)"/>
    <circle cx="246" cy="16" r="7" fill="var(--paper)"/>
  </svg>
  <section class="piece envelope" aria-label="Envelope">
    <div class="faint-disc"></div>
    <div class="wordmark"><span class="mark-dot"></span>SILVER PINE</div>
    <div class="envelope-window"></div>
    <p class="envelope-footer">4718 Wexley Lane, Golden, Colorado 80401 &nbsp;|&nbsp; P · 303-555-0148 &nbsp;|&nbsp; www.silverpinenviroq.com</p>
  </section>

  <!-- Letterhead -->
  <section class="piece letterhead" aria-label="Letterhead">
    <div class="wordmark"><span class="mark-dot"></span>SILVER PINE</div>
    <div class="letterhead-rule"></div>
    <div class="faint-disc"></div>
    <p class="letterhead-footer">4718 Wexley Lane, Golden, Colorado 80401 &nbsp;|&nbsp; P · 303-555-0148 &nbsp;|&nbsp; www.silverpinenviroq.com</p>
  </section>

  <!-- Business card front -->
  <section class="piece card-front" aria-label="Business card front">
    <div class="wordmark"><span class="mark-dot"></span>SILVER PINE</div>
    <div class="card-details">
      <p class="card-name">Tom Feaster, P.G.</p>
      <p class="card-role">Founder</p>
      <p class="card-address">4718 Wexley Lane<br>Golden, Colorado 80401</p>
      <p>P · 303-555-0148</p>
      <p>E · tfeaster@silverpinenviroq.com</p>
    </div>
  </section>

  <!-- Business card back -->
  <section class="piece card-back" aria-label="Business card back">
    <div class="faint-disc"></div>
    <p class="card-web">www.silverpinenviroq.com</p>
  </section>

</body>
</html>
```